Business card design for Velvet Harbor

We need business cards designed for our new marketing consulting company, Velvet Harbor. Our services include marketing strategy, go-to-market and launch planning, growth strategy, and execution. We serve medical technology and health technology companies, from startups to well-established growth companies.

The business cards should feel professional, credible, reliable and trustworthy, and should instill confidence. Also bold, creative, and modern.

The design must use the Velvet Harbor logo.

The primary brand color is this orange: #FF5501
A secondary color that you can use is this gray: #282B2D
I would prefer only to use the orange and gray. But if you feel you really need an additional accent color (please use it very sparingly, as little as possible), you can use this blue for small accent purposes: #009FED

Attached are the logo files. The main logo is the one with a little bit of orange on the left and the rest is gray.

The business card should include the following:

Velvet Harbor logo
First name and last name
Title
Email address
Phone number and type (in whatever order looks best for the design
Website (the website does not need to be in the same block as the personal info)

For example:

Nessa Pryle
Founder & Principal
nessa@velvetharbor.com
+1.628.309.4156 mobile (can use "." or spaces in between blocks of numbers)
velvetharbor.com (somewhere on the card, it does not need to be with the personal info; and note that there is no "www." at the beginning)

Note that there will be no address listed on the business card.

Target Market(s)

Executives (CEO, head of marketing, head of sales) at medical technology and health technology companies, mostly in their 40s and older, well-educated, often with advanced degrees. They are strategic thinkers, responsible for budgets, and familiar with P&L. Their comfort with and trust in using outside consultants varies.

Industry/Entity Type

Medical technology and health technology companies.

Contact Information for Business Card

See project description

Font styles to use
Sans Serif

Requirements
Must have
• Logo and see Business card details section above.

```html
<!DOCTYPE html>
<html lang="en">
<head>
<meta charset="UTF-8">
<title>Velvet Harbor — Business Card</title>
<link href="https://fonts.googleapis.com/css2?family=Montserrat:wght@400;500;600&display=swap" rel="stylesheet">
<style>
  :root {
    --backdrop: #1b1c1d;
    --card: #282b2d;
    --orange: #ff5501;
    --white: #f4f4f4;
    --text-soft: #e6e6e6;
  }
  * { box-sizing: border-box; margin: 0; padding: 0; }
  html, body {
    width: 1200px;
    height: 1059px;
    overflow: hidden;
    background: var(--backdrop);
    font-family: "Montserrat", sans-serif;
  }
  .canvas {
    position: relative;
    width: 1200px;
    height: 1059px;
  }
  .card {
    position: absolute;
    left: 255px;
    width: 690px;
    height: 392px;
    background: var(--card);
    border-radius: 20px;
    overflow: hidden;
  }
  .card-front { top: 89px; }
  .card-back { top: 547px; }

  /* Wordmark */
  .wordmark {
    position: absolute;
    display: flex;
    align-items: center;
  }
  .wordmark-dot {
    border-radius: 50%;
    background: var(--orange);
    flex: none;
  }
  .wordmark-name {
    color: var(--white);
    font-weight: 600;
    text-transform: uppercase;
    line-height: 1;
  }
  .wordmark-name span { display: block; }

  .card-front .wordmark {
    right: 44px;
    top: 72px;
    gap: 18px;
  }
  .card-front .wordmark-dot { width: 14px; height: 14px; }
  .card-front .wordmark-name { font-size: 22px; letter-spacing: 8px; }
  .card-front .wordmark-name span + span { margin-top: 6px; }

  .card-back .wordmark {
    left: 50%;
    top: 50%;
    transform: translate(-50%, -50%);
    gap: 30px;
  }
  .card-back .wordmark-dot { width: 26px; height: 26px; }
  .card-back .wordmark-name { font-size: 40px; letter-spacing: 14px; }
  .card-back .wordmark-name span + span { margin-top: 12px; }

  /* Front details */
  .accent-tab {
    position: absolute;
    left: 0;
    top: 192px;
    width: 21px;
    height: 42px;
    background: var(--orange);
    border-radius: 0 5px 5px 0;
  }
  .person {
    position: absolute;
    left: 44px;
    top: 190px;
  }
  .person-name {
    color: var(--orange);
    font-weight: 600;
    font-size: 26px;
    line-height: 1;
    text-transform: uppercase;
    letter-spacing: 0.5px;
  }
  .person-title {
    margin-top: 6px;
    color: var(--text-soft);
    font-weight: 400;
    font-size: 17px;
    letter-spacing: 0.4px;
  }
  .contact-list {
    position: absolute;
    left: 44px;
    top: 267px;
    list-style: none;
  }
  .contact-item {
    display: flex;
    align-items: center;
    gap: 8px;
    height: 29.5px;
    color: var(--text-soft);
    font-size: 17px;
    letter-spacing: 0.4px;
  }
  .contact-icon {
    width: 13px;
    height: 13px;
    flex: none;
    fill: var(--orange);
  }
</style>
</head>
<body>
<main class="canvas">

  <section class="card card-front" aria-label="Business card front">
    <div class="wordmark">
      <span class="wordmark-dot"></span>
      <div class="wordmark-name"><span>Velvet</span><span>Harbor</span></div>
    </div>

    <div class="accent-tab"></div>
    <div class="person">
      <h1 class="person-name">Nessa Pryle</h1>
      <p class="person-title">Founder &amp; Principal</p>
    </div>

    <ul class="contact-list">
      <li class="contact-item">
        <svg class="contact-icon" viewBox="0 0 16 16" aria-hidden="true">
          <path d="M1 5.5C1 3.5 4 2 8 2s7 1.5 7 3.5V7h-3.5V5.5h-7V7H1z"/>
          <path d="M4 8l1.5-2h5L12 8v5.5H4z"/>
        </svg>
        <span>+1 628 309 4156</span>
      </li>
      <li class="contact-item">
        <svg class="contact-icon" viewBox="0 0 16 16" aria-hidden="true">
          <path d="M1 6.5L8 1.5l7 5V15H1z"/>
          <path d="M2.5 7.5L8 11.5l5.5-4" fill="none" stroke="#282b2d" stroke-width="1.2"/>
        </svg>
        <span>nessa@velvetharbor.com</span>
      </li>
      <li class="contact-item">
        <svg class="contact-icon" viewBox="0 0 16 16" aria-hidden="true">
          <circle cx="8" cy="8" r="7"/>
          <path d="M5 3.5c1.5 1 2 2 1 3.2S7 9 8.5 9.5 9 12.5 8 14M11 3c-.8 1.2 0 2.4 1.4 2.6S14 7 14.5 8" fill="none" stroke="#282b2d" stroke-width="1.1"/>
        </svg>
        <span>velvetharbor.com</span>
      </li>
    </ul>
  </section>

  <section class="card card-back" aria-label="Business card back">
    <div class="wordmark">
      <span class="wordmark-dot"></span>
      <div class="wordmark-name"><span>Velvet</span><span>Harbor</span></div>
    </div>
  </section>

</main>
</body>
</html>
```